Design Landing Page and User Interface for Online Second Hand Merchandice Store in Web 2.0 type pa

We are creating a company which delivers second hand merchandise locally. We'd like to have a landing page developed in the web 2.0 parallax scrolling web 2.0 style. We have a design style in mind. We need to have other pages within the website designed also. However, we need to get the landing page correct first.

In the center of the landing page, there will be the Second Hand Copper Lantern Copper Lantern logo. Underneath that logo, there will be an entry to enter your email and underneath that entry, there will be an entry to enter your password. Then there will be a login button. This will be the top layer of the landing page and it will be "transparent".

The second layer of the landing page, will be "behind" the logo and login. On this second layer, there will be boxes that will have pictures of items for sale such furniture, ipods, lamps, books, CD's, TV, couches, beds. The boxes will flip over randomly and then the price for the item will be shown on the flip side of the box. If a user clicks on the box to find the price.

Scrolling down the landing Page – When you scroll down the landing page, you will see a little info graphic, which will show you how the service works. This is kind of an emulation of the Wavelore.example website which is pretty clean and looks nice.

At the bottom of the landing page you will have the menu that will have the same items as the Quillnest landing page. This will pretty much allow users to get anywhere they need to in the site. This will also serve as a guide to you to how to design architect and build everything onward from here.

NOTE: THE LANDING PAGE WILL ONLY BE SKETCH PAGES 1-4

Target Market(s)

The customers will be hipsters who live in artsy neighborhoods in the United States. The customers are cost conscious and like to save money, but also appreciate style and are also very tech savvy. The ride bicycles and are into recycling and doing helping the environment.

Industry/Entity Type

Architect

Requirements
Must have
• The website design must have the parallax scrolling style. The landing page must have our company logo on it. The logo of the company name is attached in this brief. The logo reads Second Hand Copper Lantern.

Nice to have
• A cool modern look. Imagine if Flutterbox opened up a Second Hand Goods store. That's what I want it to look like.
Should not have
• An early 2000's or mid 2000's style of design.

```html
<!DOCTYPE html>
<html lang="en">
<head>
<meta charset="utf-8">
<title>Copper Lantern Trading Post</title>
<link href="https://fonts.googleapis.com/css2?family=Open+Sans:wght@400;600;700&display=swap" rel="stylesheet">
<style>
:root{
  --maroon:#7b1d16;
  --maroon-dark:#5e140f;
  --teal:#2f7d75;
  --teal-band:#3e6a63;
  --paper:#f3f1ef;
  --ink:#3a3a3a;
  --muted:#6b6b6b;
  --rose:#b97d70;
  --panel:#e9e2de;
  --footer:#3b3b3b;
  --tick:#3d9a4a;
}
*{box-sizing:border-box;margin:0;padding:0}
html,body{width:1200px;height:3422px;overflow:hidden}
body{position:relative;font-family:"Open Sans",Arial,sans-serif;color:var(--ink);background:#d9d6d3}
.abs{position:absolute}

/* bands */
.band{position:absolute;left:0;width:1200px}
.hero{top:0;height:680px;background:linear-gradient(120deg,#8d8a80 0%,#77746d 45%,#8a8f86 80%,#7f877c 100%)}
.sell{top:600px;height:790px;background:linear-gradient(180deg,#f1efed,#e4e1de);clip-path:polygon(0 5%,100% 0,100% 100%,0 97%)}
.buy{top:1320px;height:700px;background:linear-gradient(180deg,#4a706a,#3b625b);clip-path:polygon(0 4%,100% 0,100% 100%,0 97%)}
.econ{top:1990px;height:740px;background:linear-gradient(180deg,#f4f2f0,#e6e3e0);clip-path:polygon(0 0,100% 3%,100% 100%,0 97%)}
.faqband{top:2700px;height:680px;background:linear-gradient(160deg,#c48a7c,#ad7063 60%,#b9806f);clip-path:polygon(0 3%,100% 0,100% 100%,0 100%)}
.crowd{position:absolute;left:0;width:1200px;opacity:.35;background:
  radial-gradient(ellipse 90px 300px at 10% 60%,#8f8a86,transparent),
  radial-gradient(ellipse 90px 300px at 30% 55%,#8f8a86,transparent),
  radial-gradient(ellipse 90px 300px at 60% 58%,#8f8a86,transparent),
  radial-gradient(ellipse 90px 300px at 82% 55%,#8f8a86,transparent)}

/* hero */
.tile{position:absolute;background:linear-gradient(135deg,#a89682,#6e5b4a);border:2px solid rgba(255,255,255,.35)}
.login-card{position:absolute;left:312px;top:87px;width:562px;height:442px;background:#fff;box-shadow:0 4px 18px rgba(0,0,0,.25)}
.brand{position:absolute;left:0;width:100%;top:70px;text-align:center}
.brand-dot{display:inline-block;width:146px;height:146px;border-radius:50%;border:4px solid var(--maroon);background:#fbf7f2;line-height:138px;font-weight:700;color:var(--maroon);font-size:17px}
.tagline{position:absolute;top:222px;width:100%;text-align:center;font-size:17px;color:#333}
.btn-login{position:absolute;left:46px;top:287px;width:153px;height:37px;background:var(--maroon);color:#fff;font-size:15px;display:flex;align-items:center;justify-content:center;gap:8px;border:1px solid #4a0d09}
.or{position:absolute;left:238px;top:284px;font-size:28px;color:#888;font-weight:400}
.btn-friend{position:absolute;left:320px;top:287px;width:194px;height:37px;background:#3b5a99;color:#fff;display:flex;align-items:center;padding-left:12px;gap:10px}
.btn-friend b{font-size:14px;font-weight:600}
.btn-friend small{display:block;font-size:9px;opacity:.85}
.friend-sq{width:22px;height:22px;background:#fff}
.mascot{position:absolute;left:935px;top:433px;width:92px;height:228px;border-radius:40px 40px 10px 10px;background:linear-gradient(180deg,#d7c6a4,#a35a4c 55%,#3a3a3a 85%,#e6d23a)}

/* shared */
.section-title{position:absolute;left:50%;transform:translateX(-50%);height:50px;padding:0 30px;background:#fff;border:1px solid #c9c2bd;border-bottom:3px solid var(--maroon);display:flex;align-items:center;font-size:20px;color:var(--teal);white-space:nowrap}
.cta{position:absolute;left:502px;width:196px;height:41px;background:var(--maroon);color:#fff;font-size:18px;display:flex;align-items:center;justify-content:center;gap:10px;border:1px solid var(--maroon-dark)}
.cta svg{width:20px;height:20px}
.down{position:absolute;left:581px;width:38px;height:38px}

/* sell steps */
.step{position:absolute;width:240px;text-align:center;top:853px}
.step-icon{width:110px;height:110px;border-radius:50%;border:4px solid var(--maroon);background:#fff;margin:0 auto;display:flex;align-items:center;justify-content:center}
.step h3{margin-top:22px;font-size:20px;font-weight:400;color:var(--teal)}
.step p{margin-top:10px;font-size:11.5px;line-height:1.6;color:#444;padding:0 8px}

/* buy columns */
.buycol{position:absolute;top:1540px;width:274px;color:#fff}
.buycol h4{font-size:12.5px;font-weight:700;letter-spacing:.2px;margin-bottom:8px}
.buycol .photo{height:176px}
.buycol p{margin-top:10px;font-size:12px;line-height:1.45}

/* economics */
.econ-copy{position:absolute;left:178px;top:2180px;width:430px;font-size:12px;line-height:1.55;color:#555}
.econ-copy p{margin-bottom:16px}

/* benefits / faq */
.panel{position:absolute;top:2835px;height:320px;background:var(--panel);box-shadow:0 1px 3px rgba(0,0,0,.15)}
.panel-head{margin:18px auto 0;height:40px;border:1px solid #b7aca6;border-bottom:3px solid var(--maroon);background:#fff;color:var(--teal);font-size:20px;display:flex;align-items:center;justify-content:center}
.benefits ul{list-style:none;margin:14px 22px 0 22px}
.benefits li{display:flex;gap:12px;font-size:11.5px;line-height:1.4;color:#555;margin-bottom:7px}
.benefits li svg{flex:0 0 16px;margin-top:1px}
.faq-item{margin:16px 20px 0}
.faq-item h5{font-size:12px;font-weight:400;color:var(--maroon);margin-bottom:8px}
.faq-item p{font-size:11px;line-height:1.45;color:#666;padding-bottom:16px;border-bottom:1px solid #cfc5c0}
.faq-item:last-child p{border-bottom:none}

/* footer */
.site-footer{position:absolute;left:0;top:3371px;width:1200px;height:51px;background:var(--footer);color:#ddd;font-size:11px;display:flex;align-items:center;justify-content:space-between;padding:0 178px}
.site-footer nav span{margin-right:10px}
.site-footer nav i{font-style:normal;margin-right:10px;color:#999}
</style>
</head>
<body>

<!-- hero -->
<section class="band hero">
  <div class="tile" style="left:189px;top:114px;width:123px;height:148px" role="img" aria-label="Wooden furniture for sale"></div>
  <div class="tile" style="left:189px;top:278px;width:123px;height:144px;background:linear-gradient(135deg,#7fa2b5,#4d6c7c)" role="img" aria-label="Electronics for sale"></div>
  <div class="tile" style="left:874px;top:114px;width:136px;height:148px;background:linear-gradient(90deg,#3d7a9a,#c9a53a,#5a8a3a,#b84a3a)" role="img" aria-label="Books on a shelf for sale"></div>
  <div class="tile" style="left:874px;top:278px;width:136px;height:144px;background:linear-gradient(135deg,#b58f6b,#6d4e38)" role="img" aria-label="Bed for sale"></div>

  <div class="login-card">
    <div class="brand"><span class="brand-dot">Copper Lantern</span></div>
    <p class="tagline">Buy And Sell Stuff to People.Who Know People You Know</p>
    <div class="btn-login">
      <svg width="14" height="14" viewBox="0 0 14 14"><circle cx="7" cy="4" r="3.2" fill="#fff"/><path d="M1 14c0-4 2.6-6 6-6s6 2 6 6z" fill="#fff"/></svg>Login
    </div>
    <div class="or">OR</div>
    <div class="btn-friend"><span class="friend-sq"></span><span><b>Friendlink</b><small>Sign up through Friendlink</small></span></div>
  </div>

  <div class="mascot" role="img" aria-label="Hipster mascot character"></div>
  <svg class="down" style="top:576px" viewBox="0 0 38 38"><circle cx="19" cy="19" r="17" fill="none" stroke="#9b7d72" stroke-width="2"/><path d="M12 15l7 9 7-9z" fill="#9b7d72"/></svg>
</section>

<!-- how it works to sell -->
<section class="band sell">
  <div class="crowd" style="top:60px;height:700px" role="img" aria-label="Blurred group of people"></div>
</section>
<div class="section-title" style="top:721px">How It Works To Sell</div>

<div class="step" style="left:199px">
  <div class="step-icon"><svg width="52" height="44" viewBox="0 0 52 44"><rect x="14" y="14" width="34" height="24" fill="var(--maroon)"/><path d="M14 14l17 13 17-13" fill="none" stroke="#fff" stroke-width="2"/><path d="M4 6l14 8-6 3z" fill="var(--maroon)"/></svg></div>
  <h3>Post Your Stuff</h3>
  <p>Lorem Ipsum is simply dummy text of the printing and typesetting industry. Lorem Ipsum has been the industry's standard dummy text ever since the 1500s. has survived not only five centuries unchanged.</p>
</div>
<div class="step" style="left:480px">
  <div class="step-icon"><svg width="58" height="34" viewBox="0 0 58 34"><path d="M2 14c10-6 22-6 30-2h14c4 0 4 5 0 5H32c8 2 14 0 24-6v10c-10 8-30 12-54 3z" fill="var(--maroon)"/></svg></div>
  <h3>Get Offers</h3>
  <p>Lorem Ipsum is simply dummy text of the printing and typesetting industry. Lorem Ipsum has been the industry's standard dummy text ever since the 1500s. has survived not only five centuries unchanged.</p>
</div>
<div class="step" style="left:754px">
  <div class="step-icon"><svg width="44" height="44" viewBox="0 0 44 44"><rect x="4" y="20" width="9" height="20" fill="var(--maroon)"/><path d="M16 20l8-16c4 0 5 3 4 7l-2 7h12c3 0 4 3 3 5l-4 14c-1 2-2 3-4 3H16z" fill="var(--maroon)"/></svg></div>
  <h3>Pick Up</h3>
  <p>Lorem Ipsum is simply dummy text of the printing and typesetting industry. Lorem Ipsum has been the industry's standard dummy text ever since the 1500s. has survived not only five centuries unchanged.</p>
</div>

<div class="cta" style="top:1198px"><svg viewBox="0 0 20 20"><circle cx="10" cy="10" r="9" fill="#fff"/><path d="M10 4l5 6h-3v5H8v-5H5z" fill="var(--maroon)"/></svg>Sign Up Now!</div>
<svg class="down" style="top:1277px" viewBox="0 0 38 38"><circle cx="19" cy="19" r="17" fill="none" stroke="var(--teal-band)" stroke-width="2"/><path d="M12 15l7 9 7-9z" fill="var(--teal-band)"/></svg>

<!-- how it works to buy -->
<section class="band buy">
  <div class="crowd" style="top:40px;height:640px;opacity:.25" role="img" aria-label="Blurred group of people"></div>
</section>
<div class="section-title" style="top:1405px">How It Works To Buy</div>

<div class="buycol" style="left:178px">
  <h4>BROWSE BY SECTION</h4>
  <div class="photo" role="img" aria-label="Shopper holding bags" style="background:linear-gradient(135deg,#c9a27a,#7b8f9a 60%,#4f6f86)"></div>
  <p>Lorem Ipsum is simply dummy text of the printing and typesetting industry. Lorem Ipsum has been the industry's standard dummy text ever since the 1500s.</p>
</div>
<div class="buycol" style="left:463px">
  <h4>BUY URGENT</h4>
  <div class="photo" role="img" aria-label="Busy travellers in a hall" style="background:linear-gradient(135deg,#d9d6d2,#8c8580 55%,#5a4f4a)"></div>
  <p>Lorem Ipsum is simply dummy text of the printing and typesetting industry. Lorem Ipsum has been the industry's standard dummy text ever since the 1500s.</p>
</div>
<div class="buycol" style="left:748px">
  <h4>SET UP TIME FOR DELIVERY</h4>
  <div class="photo" role="img" aria-label="Courier with parcel and clock" style="background:linear-gradient(135deg,#e7e3dc,#b09a78 55%,#6f6a66)"></div>
  <p>Lorem Ipsum is simply dummy text of the printing and typesetting industry. Lorem Ipsum has been the industry's standard dummy text ever since the 1500s.</p>
</div>

<div class="cta" style="top:1873px"><svg viewBox="0 0 20 20"><circle cx="10" cy="10" r="9" fill="#fff"/><path d="M10 4l5 6h-3v5H8v-5H5z" fill="var(--maroon)"/></svg>Sign Up Now!</div>
<svg class="down" style="top:1952px" viewBox="0 0 38 38"><circle cx="19" cy="19" r="17" fill="none" stroke="#b9c9c6" stroke-width="2"/><path d="M12 15l7 9 7-9z" fill="#b9c9c6"/></svg>

<!-- neighbourhood economics -->
<section class="band econ">
  <div class="crowd" style="top:60px;height:660px" role="img" aria-label="Blurred group of people"></div>
</section>
<div class="section-title" style="top:2064px">Neighbourhood Economics Benefits</div>

<div class="econ-copy">
  <p>Lorem Ipsum is simply dummy text of the printing and typesetting industry. Lorem Ipsum has been the industry's standard dummy text ever since the 1500s, when an unknown printer took a galley of type and scrambled it to make a type specimen book. It has survived not only five centuries, but also the leap into electronic typesetting, remaining essentially unchanged.</p>
  <p>Lorem Ipsum is simply dummy text of the printing and typesetting industry. Lorem Ipsum has been the industry's standard dummy text ever since the 1500s, when an unknown printer took a galley of type and scrambled it to make a type specimen book. It has survived not only five centuries, but also the leap into electronic typesetting, remaining essentially unchanged.</p>
  <p>Lorem Ipsum is simply dummy text of the printing and typesetting industry. Lorem Ipsum has been the industry's standard</p>
</div>

<svg class="abs" style="left:680px;top:2170px" width="360" height="320" viewBox="0 0 360 320" font-family="Open Sans, sans-serif" font-size="8" fill="#555">
  <g stroke="#777" stroke-width=".8" fill="none">
    <path d="M125 86L70 30H30"/><path d="M195 86L240 50H290"/><path d="M205 120L240 120H300"/>
    <path d="M110 125L60 125H20"/><path d="M140 150L110 190H70"/><path d="M245 245L225 225H190"/><path d="M100 280L70 265"/>
  </g>
  <circle cx="159" cy="111" r="38" fill="none" stroke="#3ab0b8" stroke-width="16"/>
  <path d="M159 73a38 38 0 0 1 38 38" fill="none" stroke="#2a8c93" stroke-width="16"/>
  <circle cx="253" cy="248" r="20" fill="none" stroke="#3aa7ad" stroke-width="9"/>
  <circle cx="93" cy="273" r="20" fill="none" stroke="#3aa7ad" stroke-width="9"/>
  <path d="M93 253a20 20 0 0 1 20 20" fill="none" stroke="#1f7f86" stroke-width="9"/>
  <text x="30" y="22">Details of statistics.</text><text x="30" y="32">Description of statistics.</text>
  <text x="220" y="42">Details of statistics.</text><text x="220" y="52">Description of statistics.</text>
  <text x="240" y="112">Details of statistics.</text><text x="240" y="122">Description of statistics.</text>
  <text x="15" y="118">Details of statistics.</text><text x="15" y="128">Description of statistics.</text>
  <text x="70" y="184">Details of statistics.</text><text x="70" y="194">Description of statistics.</text>
  <text x="170" y="218" font-size="6">Details of statistics</text>
  <text x="280" y="222" font-size="6">Details of statistics</text>
  <text x="20" y="262" font-size="6">Details of statistics</text>
</svg>

<div class="cta" style="top:2562px"><svg viewBox="0 0 20 20"><circle cx="10" cy="10" r="9" fill="#fff"/><path d="M10 4l5 6h-3v5H8v-5H5z" fill="var(--maroon)"/></svg>Sign Up Now!</div>
<svg class="down" style="top:2634px" viewBox="0 0 38 38"><circle cx="19" cy="19" r="17" fill="none" stroke="var(--teal-band)" stroke-width="2"/><path d="M12 15l7 9 7-9z" fill="var(--teal-band)"/></svg>

<!-- benefits and faq -->
<section class="band faqband">
  <div class="crowd" style="top:40px;height:600px;opacity:.2" role="img" aria-label="Blurred background scene"></div>
</section>
<div class="section-title" style="top:2749px">Benefits of Buy &amp; Selling on the Post</div>

<div class="panel benefits" style="left:176px;width:495px">
  <div class="panel-head" style="width:310px">BENEFITS</div>
  <ul>
    <li><svg width="16" height="14" viewBox="0 0 16 14"><path d="M1 7l5 5L15 1" fill="none" stroke="var(--tick)" stroke-width="2.5"/></svg>Lorem Ipsum is simply dummy text of the printing and typesetting industry.</li>
    <li><svg width="16" height="14" viewBox="0 0 16 14"><path d="M1 7l5 5L15 1" fill="none" stroke="var(--tick)" stroke-width="2.5"/></svg>Lorem Ipsum is simply dummy text of the printing and typesetting industry. Lorem Ipsum has been the industry's standard dummy text ever Since the 1500s.</li>
    <li><svg width="16" height="14" viewBox="0 0 16 14"><path d="M1 7l5 5L15 1" fill="none" stroke="var(--tick)" stroke-width="2.5"/></svg>Lorem Ipsum is simply dummy text of the printing and typesetting industry.</li>
    <li><svg width="16" height="14" viewBox="0 0 16 14"><path d="M1 7l5 5L15 1" fill="none" stroke="var(--tick)" stroke-width="2.5"/></svg>Lorem Ipsum is simply dummy text of the printing and typesetting industry.</li>
    <li><svg width="16" height="14" viewBox="0 0 16 14"><path d="M1 7l5 5L15 1" fill="none" stroke="var(--tick)" stroke-width="2.5"/></svg>Lorem Ipsum is simply dummy text of the printing and typesetting industry. Lorem Ipsum has been the industry's standard dummy text ever since the 1500s.</li>
    <li><svg width="16" height="14" viewBox="0 0 16 14"><path d="M1 7l5 5L15 1" fill="none" stroke="var(--tick)" stroke-width="2.5"/></svg>Lorem Ipsum is simply dummy text of the printing and typesetting industry.</li>
    <li><svg width="16" height="14" viewBox="0 0 16 14"><path d="M1 7l5 5L15 1" fill="none" stroke="var(--tick)" stroke-width="2.5"/></svg>Lorem Ipsum is simply dummy text of the printing and typesetting industry.</li>
  </ul>
</div>

<div class="panel faq" style="left:680px;width:344px">
  <div class="panel-head" style="width:196px">FAQ</div>
  <div class="faq-item">
    <h5>Sed Ut Perspiciatis Unde Omnis Iste Natus Error Sit?</h5>
    <p>Voluptatem accusantium doloremque laudantium, totam rem aperiam, eaque ipsa quae ab illo inventore veritatis et quasi architecto beatae vitae dicta sunt explicabo. Nemo enim ipsam.</p>
  </div>
  <div class="faq-item">
    <h5>Sed Ut Perspiciatis Unde Omnis Iste Natus Error Sit?</h5>
    <p>Voluptatem accusantium doloremque laudantium, totam rem aperiam, eaque ipsa quae ab illo inventore veritatis et quasi architecto beatae vitae dicta sunt explicabo. Nemo enim ipsam.</p>
  </div>
</div>

<div class="cta" style="top:3210px"><svg viewBox="0 0 20 20"><circle cx="10" cy="10" r="9" fill="#fff"/><path d="M10 4l5 6h-3v5H8v-5H5z" fill="var(--maroon)"/></svg>Sign Up Now!</div>
<svg class="down" style="top:3293px" viewBox="0 0 38 38"><circle cx="19" cy="19" r="17" fill="none" stroke="#8a4a40" stroke-width="2"/><path d="M12 15l7 9 7-9z" fill="#8a4a40"/></svg>

<footer class="site-footer">
  <nav><span>Privacy policy</span><i>|</i><span>Terms &amp; Condition</span><i>|</i><span>Contact Us</span></nav>
  <span>©2014 Copper Lantern Trading Post. All rights reserved.</span>
</footer>

</body>
</html>
```